Project Management - Web Design Project

Valtrix 4 Management Limited is a company which provides specialist Project Control and Contract Management expertise to the Engineering, Construction and Manufacturing industries. The emphasis is on advanced Project Management techniques in particular Planning & Scheduling, Cost Control, Change Control, Risk Management, Reporting and Contract Administration. We are a global company (albeit a small start-up at this time) and pride ourselves on our ability to support projects to help them achieve their goals and objectives. Our aim is to implement work class control tools in a simple and user friendly manner. We would like the website to appear professional but at the same time easy to navigate and a good balance between text and pictures. The final design should communicate our value added service to our customers, our willingness to support and our structured approach to our work.

Target Market(s)

Project Management professionals working for engineering, construction and manufacturing organisations involved with delivering projects.

Industry/Entity Type

Construction

Requirements
Must have
• The website must include all of the content from the attached Excel brief. The company logo (attached) must also be included in the design. The design must portray a professional look and feel. Please include pictures and photographs related to project management in the engineering, construction and manufacturing industries. We may supplement with pictures of our own during the next steps.
Nice to have
• Emphasis that Valtrix 4 is available to support, guide, direct to achieve positive outcomes for the projects. We work hard at developing our customer relationships. Our employees are experienced in advanced project management techniques.
Should not have
• The design should not use old style fonts. It should look modern and professional. Do not include cartoons or silly illustrations.

```html
<!DOCTYPE html>
<html lang="en">
<head>
<meta charset="utf-8">
<title>Valtrix 4 Management Limited</title>
<link href="https://fonts.googleapis.com/css2?family=Ubuntu:wght@300;400;500&display=swap" rel="stylesheet">
<style>
:root{
  --brand-blue:#2b86e0;
  --nav-text:#3a3f47;
  --logo-grey:#5a5f66;
  --panel:#474c56;
  --panel-line:#5d626c;
  --accent:#f4a81d;
  --muted:#8a8f98;
  --white:#ffffff;
  --footer:#060606;
  --hero-a:#e9edf1;
  --hero-b:#8f979f;
  --card-blue:rgba(52,128,214,.86);
}
*{margin:0;padding:0;box-sizing:border-box}
html,body{width:1158px;height:1200px;overflow:hidden;background:var(--white)}
body{font-family:'Ubuntu',sans-serif;font-weight:300;color:var(--nav-text);position:relative}
.top-bar{position:absolute;left:0;top:0;width:1158px;height:6px;background:var(--brand-blue)}
.header{position:absolute;left:0;top:6px;width:1158px;height:150px;background:var(--white)}
.logo{position:absolute;left:115px;top:14px;display:flex;flex-direction:column;align-items:center;width:156px}
.logo-mark{width:70px;height:70px;border-radius:50%;background:var(--logo-grey)}
.logo-name{margin-top:10px;font-size:24px;font-weight:400;color:var(--logo-grey);letter-spacing:1px}
.logo-sub{font-size:10px;font-weight:400;color:var(--logo-grey);letter-spacing:1.6px}
.call-line{position:absolute;right:119px;top:12px;font-size:16px;color:var(--brand-blue)}
.call-line strong{font-weight:500}
.main-nav{position:absolute;right:110px;top:106px;display:flex;font-size:15px;letter-spacing:-.3px}
.main-nav a{color:var(--nav-text);text-decoration:none;padding:0 12px;border-left:2px solid var(--nav-text);line-height:16px}
.main-nav a:first-child{border-left:0;color:var(--brand-blue)}
.hero{position:absolute;left:0;top:156px;width:1158px;height:444px;background:linear-gradient(100deg,var(--hero-a) 0%,#c8cdd3 35%,#4c5159 55%,#363a42 70%,var(--hero-b) 100%)}
.hero-card{position:absolute;left:107px;top:102px;width:431px;height:193px;background:var(--card-blue);border-radius:5px;padding:14px 13px;color:var(--white)}
.hero-card h1{font-size:26px;font-weight:500;margin-bottom:14px;letter-spacing:-.3px}
.hero-card p{font-size:13.2px;line-height:16.3px;letter-spacing:-.3px}
.hero-card a{display:inline-block;margin-top:14px;font-size:14.5px;color:#111;text-decoration:underline;font-weight:300}
.panel{position:absolute;left:0;top:600px;width:1158px;height:542px;background:var(--panel)}
.section-title{position:absolute;font-size:19px;font-weight:500;color:var(--accent)}
.service{position:absolute;top:69px;width:180px}
.service-photo{width:180px;height:82px}
.service h3{margin-top:7px;font-size:13.5px;font-weight:400;color:var(--white);padding-left:2px}
.service p{margin-top:11px;font-size:12.5px;line-height:15px;color:var(--muted);letter-spacing:.2px}
.service .more{position:absolute;top:183px;font-size:14px;color:var(--white);text-decoration:underline}
.pager{position:absolute;left:315px;top:297px;width:70px;height:18px;border-radius:3px;background:#5f646e}
.divider{position:absolute;left:728px;top:62px;width:1px;height:290px;background:var(--panel-line)}
.deliverables{position:absolute;left:760px;top:66px;list-style:disc;color:var(--white);font-size:14.5px;line-height:23.2px;padding-left:0}
.newsletter{position:absolute;left:748px;top:281px;width:291px;height:25px;border-radius:13px;background:var(--white);font-size:13.5px;color:var(--nav-text);padding-left:50px;line-height:25px}
.newsletter svg{position:absolute;left:17px;top:7px}
.social{position:absolute;left:760px;top:320px;display:flex;gap:18px}
.social span{width:30px;height:30px;border-radius:4px;display:block}
.admin-text{position:absolute;left:107px;top:400px;width:940px;font-size:14.5px;line-height:17.4px;color:var(--white);letter-spacing:-.25px}
.footer{position:absolute;left:0;top:1142px;width:1158px;height:58px;background:var(--footer);color:var(--white);font-size:12px;font-weight:400}
.footer .copy{position:absolute;left:110px;top:22px;font-family:Arial,sans-serif}
.footer .legal{position:absolute;right:118px;top:23px}
</style>
</head>
<body>
<div class="top-bar"></div>
<header class="header">
  <div class="logo">
    <span class="logo-mark"></span>
    <span class="logo-name">VALTRIX 4</span>
    <span class="logo-sub">MANAGEMENT LIMITED</span>
  </div>
  <div class="call-line">For a FREE &nbsp;call to contact us on : <strong>0161 496 0321</strong></div>
  <nav class="main-nav">
    <a>Home</a><a>Why work with us?</a><a>Services</a><a>Our sales Process</a><a>FAQs</a><a>Proven Success</a><a>News</a>
  </nav>
</header>

<section class="hero" role="img" aria-label="Photograph of two businessmen in suits reviewing documents">
  <div class="hero-card">
    <h1>Management Limited</h1>
    <p>Effective Contract Management is essential for a project to be success-ful. &nbsp;The contract represents the agreed rights and obligations made by each party to one another. &nbsp;In addition there may be many underlying obligations some stated explicitly in the contract while others may be implied. These obligations form the baseline frame of reference.</p>
    <a>Learn more about Valtrix 4 Management Limited</a>
  </div>
</section>

<section class="panel">
  <h2 class="section-title" style="left:108px;top:30px">Valtrix 4 Services</h2>

  <div class="service" style="left:108px">
    <div class="service-photo" role="img" aria-label="Photo of a smiling businesswoman with colleague" style="background:linear-gradient(90deg,#6b6258,#8a7aa8,#c9b69a)"></div>
    <h3>General</h3>
    <p>Contract Appraisal Meeting Responsibility Assignment Matrix Customer Supplied Deliverables</p>
    <span class="more">Read more </span>
  </div>
  <div class="service" style="left:293px">
    <div class="service-photo" role="img" aria-label="Photo of hands using a tablet" style="background:linear-gradient(90deg,#d8d8dc,#5b4a60,#e3dde6)"></div>
    <h3 style="padding-left:3px">Claims &amp; Dispute</h3>
    <p style="padding-left:3px">Schedule Claims Analysis Schedule Impact Management Notices and Claim Preparation</p>
    <span class="more" style="left:5px">Read more </span>
  </div>
  <div class="service" style="left:478px">
    <div class="service-photo" role="img" aria-label="Photo of business people in a bright office lobby" style="background:linear-gradient(90deg,#f2f3f4,#d9dcdf,#b4b8bc)"></div>
    <h3 style="padding-left:1px">Progress Payments</h3>
    <p style="padding-left:1px">Milestone Payments Progress Payments (Percent Complete) Advance Payments</p>
    <span class="more" style="left:4px">Read more </span>
  </div>

  <svg class="pager" viewBox="0 0 70 18" width="70" height="18">
    <polygon points="14,4 14,14 7,9" fill="#c9ccd1"/>
    <circle cx="28" cy="9" r="4" fill="#2f333a"/>
    <circle cx="40" cy="9" r="4" fill="#f4a81d"/>
    <polygon points="56,4 56,14 63,9" fill="#c9ccd1"/>
  </svg>

  <div class="divider"></div>
  <h2 class="section-title" style="left:759px;top:32px">Sub Contractor Deliverables</h2>
  <ul class="deliverables">
    <li>Contract Baseline Schedule</li>
    <li>Monthly Reporting Requirements</li>
    <li>Site Instructions</li>
    <li>Requests for Information (RFI)</li>
    <li>Change Requests</li>
    <li>Mobilisation Plan</li>
    <li>Resource Plans</li>
  </ul>

  <h2 class="section-title" style="left:749px;top:260px">Connect with Us</h2>
  <div class="newsletter">
    <svg width="24" height="13" viewBox="0 0 24 13"><rect x="0.5" y="0.5" width="23" height="12" fill="none" stroke="#111" stroke-width="1.5"/><polyline points="0.5,0.5 12,8 23.5,0.5" fill="none" stroke="#111" stroke-width="1.5"/></svg>
    Sign up for Our Newsletter
  </div>
  <div class="social">
    <span style="background:#c9342c"></span>
    <span style="background:#3a6fc4"></span>
    <span style="background:#2f84c0"></span>
    <span style="background:#f08a24"></span>
    <span style="background:#3b5b98"></span>
    <span style="background:#6fc6e4"></span>
  </div>

  <h2 class="section-title" style="left:107px;top:374px">Sub Contract Administration</h2>
  <p class="admin-text">Depending on the contracting arrangement adopted by the contractor certain scope may be sub contracted to a third party (sub contractor / supplier) due to the specialist nature of the work. &nbsp;In many instances the amount of work sub contracted may in fact exceed the work to be performed directly by the principal contractor. &nbsp;While the work may be sub contracted on a lump sum basis, it remains vital to the project team to manage these sub con-tractors to ensure a successful outcome for the project. &nbsp;Sub contract management (administration) is often a complex and time consuming task espe-cially if the systems and processes needed are not sufficiently mature. &nbsp;Our approach is to equip the project team with these systems and processes, procedures and tools to enable them to quickly implement the control required without expending a significant time developing a sub contract administration system.</p>
</section>

<footer class="footer">
  <span class="copy">© Valtrix 4 Services Management Limited</span>
  <span class="legal">Privacy Policy &nbsp;&nbsp;| &nbsp;&nbsp;Terms &amp; Conditions</span>
</footer>
</body>
</html>
```